Service Plan Sales Flyer

The Watchpost Depot (www.kelvamart.com) is a commercial security integrator that installs security cameras, access control, intrusion, two-way radios and perimeter security. We require a one page flyer for our service plan for new and existing customers. The price of the service plan is $299/yr and includes the following;
1. Discounted service rate of $118/hr
2. Free remote support ($85/hr without a plan)
3. Free remote training
4. Priority support

Please review our brochure attached and create a one page sales flyer with the end goal of having the client sign up for our annual service plan . The plan will automatically renew every year. Email sales@kelvamart.com.

Target Market(s)

commercial industrial clients - no residential

Industry/Entity Type

review our website at www.kelvamart.com

Colors
0054AA
0677BA
7BADD7
CADEEF
E8F1F8
EE7325
F08F49
F5BC92
FAE3D3
FDF4ED

Requirements
Must have
• call to action
Should not have
• too many colors

```html
<!DOCTYPE html>
<html lang="en">
<head>
<meta charset="utf-8">
<title>The Watchpost Depot – Service Plan</title>
<link rel="stylesheet" href="https://fonts.googleapis.com/css2?family=Bebas+Neue&family=Montserrat:wght@400;500;600;700&family=Oswald:wght@500;600;700&display=swap">
<style>
  :root {
    --navy: #0d2d5a;
    --red: #ef4234;
    --white: #ffffff;
    --ink: #1d1d1f;
    --backdrop: #bdbdbd;
    --rule: #e9eaec;
  }
  * { box-sizing: border-box; margin: 0; padding: 0; }
  html, body { width: 1200px; height: 1200px; overflow: hidden; background: var(--backdrop); }
  body { font-family: "Montserrat", sans-serif; color: var(--ink); }

  .flyer {
    position: absolute; left: 168px; top: 0;
    width: 864px; height: 1200px; background: var(--white); overflow: hidden;
  }
  .abs { position: absolute; }

  /* brand */
  .brand { left: 0; right: 0; top: 66px; display: flex; justify-content: center; align-items: center; gap: 14px; }
  .brand-dot { width: 34px; height: 34px; border-radius: 50%; background: var(--navy); }
  .brand-name { font-family: "Oswald", sans-serif; font-weight: 700; font-size: 38px; color: var(--navy); letter-spacing: .5px; text-transform: uppercase; line-height: 1; }
  .brand-tag { left: 0; right: 0; top: 114px; text-align: center; font-size: 9px; font-weight: 700; color: var(--navy); }

  /* hero */
  .plan-pill { left: 51px; top: 176px; width: 308px; height: 52px; background: var(--red); border-radius: 12px;
    color: var(--white); font-weight: 700; font-size: 33px; display: flex; align-items: center; justify-content: center; letter-spacing: .3px; }
  .plan-price { left: 49px; top: 226px; font-family: "Oswald", sans-serif; font-weight: 700; font-size: 104px; line-height: 1.05;
    color: var(--navy); letter-spacing: -1px; white-space: nowrap; transform: scaleX(.86); transform-origin: left top; }
  .plan-lead { left: 51px; top: 344px; width: 320px; font-size: 17.5px; font-weight: 500; line-height: 1.22; color: var(--ink); }
  .hero-visual { left: 397px; top: 168px; width: 420px; height: 281px; border-radius: 8px;
    background: radial-gradient(ellipse at 60% 45%, #e4e7eb 0%, #f3f4f6 55%, #ffffff 100%); }

  /* coverage list */
  .coverage { top: 470px; left: 0; width: 864px; height: 100px; }
  .coverage-rule { left: 363px; top: 14px; width: 470px; height: 17px; background: var(--rule); }
  .coverage-divider { left: 431px; top: 2px; width: 2px; height: 96px; background: var(--navy); }
  .cov-item { display: flex; align-items: center; white-space: nowrap; }
  .cov-icon { flex: none; width: 45px; height: 45px; border-radius: 50%; background: var(--navy); display: flex; align-items: center; justify-content: center; box-shadow: inset 0 0 0 3px var(--navy), inset 0 0 0 4.5px var(--white); }
  .cov-arrow { flex: none; width: 0; height: 0; border-left: 10px solid var(--red); border-top: 6px solid transparent; border-bottom: 6px solid transparent; margin-left: 8px; }
  .cov-label { font-family: "Bebas Neue", sans-serif; font-weight: 400; font-size: 27px; line-height: 1; color: var(--navy); margin-left: 18px; text-transform: uppercase; letter-spacing: 0; padding-top: 3px; }

  /* benefits band */
  .benefits { left: 0; top: 594px; width: 864px; height: 490px; background: var(--navy); }
  .card { background: var(--white); border: 2.5px solid var(--red); border-radius: 16px; padding: 18px 20px 0 22px; }
  .card-title { font-size: 21px; font-weight: 500; color: var(--navy); margin-bottom: 10px; }
  .card-title strong { color: var(--red); font-weight: 700; font-size: 23px; }
  .card-text { font-size: 15.5px; line-height: 1.27; color: var(--ink); }
  .renew { left: 0; right: 0; top: 1012px; text-align: center; color: var(--white); font-weight: 700; font-size: 20px; }
  .hours { left: 0; right: 0; top: 1050px; text-align: center; color: var(--white); font-size: 12.5px; }

  /* contact bar */
  .contact { left: 0; top: 1091px; width: 864px; height: 109px; background: var(--red); }
  .phone-box { left: 49px; top: 22px; width: 299px; height: 39px; background: var(--white); border-radius: 6px; display: flex; align-items: center; padding-left: 14px; gap: 14px; }
  .phone-number { font-weight: 700; font-size: 27px; color: var(--navy); letter-spacing: -.3px; }
  .contact-link { top: 27px; display: flex; align-items: center; gap: 9px; color: var(--white); font-weight: 700; font-size: 15px; }
  .contact-icon { width: 31px; height: 31px; border-radius: 50%; background: var(--white); display: flex; align-items: center; justify-content: center; }
</style>
</head>
<body>
<main class="flyer">

  <header class="brand abs">
    <span class="brand-dot"></span>
    <span class="brand-name">The Watchpost Depot</span>
  </header>
  <p class="brand-tag abs">Commercial &amp; Industrial Solutions</p>

  <div class="hero-visual abs" role="img" aria-label="Security equipment arrangement: a door with access reader, a monitor showing camera footage, a dome camera and a bullet camera"></div>
  <div class="plan-pill abs">SERVICE PLAN</div>
  <h1 class="plan-price abs">$299/YR</h1>
  <p class="plan-lead abs">The Tier 1 service plan gives you confidence your system will be running when you need it most.</p>

  <section class="coverage abs">
    <div class="coverage-rule abs"></div>
    <div class="coverage-divider abs"></div>

    <div class="cov-item abs" style="left:49px;top:0;">
      <span class="cov-icon">
        <svg width="22" height="22" viewBox="0 0 24 24" fill="#fff"><rect x="3" y="8" width="13" height="8" rx="1.5" transform="rotate(-15 9 12)"/><path d="M16 10l5-2v7l-5-2z"/><rect x="5" y="17" width="2" height="4"/></svg>
      </span>
      <span class="cov-arrow"></span>
      <span class="cov-label">Security Camera System</span>
    </div>
    <div class="cov-item abs" style="left:49px;top:51px;">
      <span class="cov-icon">
        <svg width="20" height="20" viewBox="0 0 24 24" fill="none" stroke="#fff" stroke-width="1.8"><rect x="5" y="2" width="14" height="20" rx="2"/><rect x="8" y="5" width="8" height="4"/><path d="M8 12h2M12 12h2M8 15h2M12 15h2M8 18h2M12 18h2"/></svg>
      </span>
      <span class="cov-arrow"></span>
      <span class="cov-label">Intrusion Alarm</span>
    </div>
    <div class="cov-item abs" style="left:513px;top:0;">
      <span class="cov-icon">
        <svg width="22" height="22" viewBox="0 0 24 24" fill="none" stroke="#fff" stroke-width="1.8"><circle cx="15" cy="8" r="4"/><path d="M12 11l-8 8M6 17l2 2M8 15l2 2"/><path d="M4 4l16 16"/></svg>
      </span>
      <span class="cov-arrow"></span>
      <span class="cov-label">Access Control &amp; Intercom</span>
    </div>
    <div class="cov-item abs" style="left:513px;top:51px;">
      <span class="cov-icon">
        <svg width="22" height="22" viewBox="0 0 24 24" fill="none" stroke="#fff" stroke-width="1.6"><path d="M3 9h18M3 14h18M3 19h18M6 6v15M10 6v15M14 6v15M18 6v15"/></svg>
      </span>
      <span class="cov-arrow"></span>
      <span class="cov-label">Perimeter Security</span>
    </div>
  </section>

  <section class="benefits abs">
    <article class="card abs" style="left:49px;top:33px;width:374px;height:152px;">
      <h2 class="card-title"><strong>Discounted</strong> service rate</h2>
      <p class="card-text">Receive a $20/hour discount on any security related services provided by The Watchpost Depot</p>
    </article>
    <article class="card abs" style="left:444px;top:33px;width:373px;height:152px;">
      <h2 class="card-title"><strong>Unlimited</strong> Remote Support</h2>
      <p class="card-text">access our highly technical security team with remote web and phone support at no charge to you</p>
    </article>
    <article class="card abs" style="left:49px;top:208px;width:374px;height:195px;">
      <h2 class="card-title"><strong>Free</strong> Remote Training</h2>
      <p class="card-text">Take advantage of our remote training sessions. Our experienced trainers will guide your existing and new managers through the operation and administration of your security system.</p>
    </article>
    <article class="card abs" style="left:444px;top:208px;width:373px;height:195px;">
      <h2 class="card-title"><strong>Priority</strong> Support</h2>
      <p class="card-text">As a service plan subscriber you will receive priority support. Your inquiries and requests will be given expedited attention ensuring prompt assistance and minimizing downtime and disruptions to your security system.</p>
    </article>
  </section>
  <p class="renew abs">Plan renews annually, cancel anytime.</p>
  <p class="hours abs">All service, training and support is Monday to Friday during normal working hours.</p>

  <footer class="contact abs">
    <div class="phone-box abs">
      <svg width="22" height="22" viewBox="0 0 24 24" fill="none" stroke="#ef4234" stroke-width="2.2" stroke-linecap="round"><path d="M5 3h3l2 5-2 1.5a11 11 0 0 0 6 6L15.5 13l5 2v3a2 2 0 0 1-2 2A16 16 0 0 1 3 5a2 2 0 0 1 2-2z"/><path d="M14 3a7 7 0 0 1 7 7M14 7a3 3 0 0 1 3 3"/></svg>
      <span class="phone-number">1-877-555-0148</span>
    </div>
    <div class="contact-link abs" style="left:383px;">
      <span class="contact-icon">
        <svg width="20" height="20" viewBox="0 0 24 24" fill="none" stroke="#0d2d5a" stroke-width="1.8"><circle cx="12" cy="12" r="9"/><path d="M3 12h18M12 3c3 3 3 15 0 18M12 3c-3 3-3 15 0 18"/></svg>
      </span>
      <span>www.kelvamart.com</span>
    </div>
    <div class="contact-link abs" style="left:616px;">
      <span class="contact-icon">
        <svg width="18" height="18" viewBox="0 0 24 24" fill="#0d2d5a"><rect x="2" y="5" width="20" height="14" rx="2"/><path d="M3 6l9 7 9-7" fill="none" stroke="#fff" stroke-width="1.8"/></svg>
      </span>
      <span>sales@kelvamart.com</span>
    </div>
  </footer>

</main>
</body>
</html>
```